Webbanner-Design für Fachhandel für Medizinprodukte
Zielgruppe
wir sind ein Fachhandel für Medizinprodukte.
Aufgabenstellung
-Slider / Banner
-1920 x 340
-Es muss ein intersannter Satz auf dem Bild sein, der einläd zu klicken.
-https://www.medivolta.de/
- folgender Artikel soll beworben werden:
-https://www.medivolta.de/fingerpulsoximeter-kx418-pulsoximeter-weiss-5912
-Design soll gut zur Seite passen.
-Das Bild kann von der Seite verwendet werden.
-Gerne können zusätzlich auch Stockbilder verarbeitet werden.

```html
<!DOCTYPE html>
<html lang="de">
<head>
<meta charset="utf-8">
<title>MEDIVOLTA – Pulsoximeter KX418</title>
<link rel="stylesheet" href="https://fonts.googleapis.com/css2?family=Montserrat:wght@700;800&display=swap">
<style>
  :root {
    --page-bg: #dfdfde;
    --banner-bg: #ececec;
    --brand-green: #3fad49;
    --text-dark: #1f1f1f;
    --white: #ffffff;
    --product-light: #f6f6f6;
    --product-shade: #cfd0d0;
  }
  * { margin: 0; padding: 0; box-sizing: border-box; }
  html, body {
    width: 1200px;
    height: 494px;
    overflow: hidden;
    background: var(--page-bg);
    font-family: "Montserrat", Arial, sans-serif;
  }
  .banner {
    position: absolute;
    left: 90px;
    top: 156px;
    width: 1021px;
    height: 180px;
    background: var(--banner-bg);
  }
  .product-image {
    position: absolute;
    left: 57px;
    top: 17px;
    width: 234px;
    height: 143px;
    border-radius: 14px;
    background: radial-gradient(ellipse at 45% 45%, var(--product-light) 0%, #e7e8e8 60%, var(--product-shade) 100%);
  }
  .model-name {
    position: absolute;
    left: 180px;
    top: 30px;
    font-weight: 800;
    font-size: 24px;
    color: var(--text-dark);
    letter-spacing: 0.5px;
  }
  .headline {
    position: absolute;
    left: 354px;
    top: 16px;
    font-weight: 800;
    font-size: 69px;
    line-height: 72px;
    color: var(--brand-green);
    letter-spacing: 0.5px;
    white-space: nowrap;
  }
  .brand-name {
    position: absolute;
    left: 800px;
    top: 27px;
    font-weight: 800;
    font-size: 27px;
    color: var(--brand-green);
    letter-spacing: 0.3px;
  }
  .cta-button {
    position: absolute;
    left: 802px;
    top: 101px;
    width: 184px;
    height: 49px;
    border-radius: 8px;
    background: var(--brand-green);
    color: var(--white);
    font-weight: 700;
    font-size: 18.5px;
    display: flex;
    align-items: center;
    justify-content: center;
    text-decoration: none;
    box-shadow: 0 2px 4px rgba(0,0,0,0.12);
  }
</style>
</head>
<body>
  <div class="banner">
    <div class="product-image" role="img" aria-label="Produktfoto: weißes Fingerpulsoximeter KX418 mit Digitalanzeige"></div>
    <div class="model-name">KX418</div>
    <h1 class="headline">SCHNELL<br>&amp; GENAUE</h1>
    <span class="brand-name">MEDIVOLTA</span>
    <a class="cta-button" href="https://www.medivolta.de/fingerpulsoximeter-kx418-pulsoximeter-weiss-5912">Jetzt Einkaufen</a>
  </div>
</body>
</html>
```